Silver Harbour Fitness

Promotional poster design for a Fun, Fresh, New functional fitness studio on the Southern Cove's in Sydney, Australia. Where we motivate, educate and concentrate on healthy living.

"We help people look and feel a million dollars".

Our colours are in the LOGO

Dimensions
A0 = 1189mm x 841mm and possibly bigger.

Target Market(s)

20-35yrs of age, female.

Industry/Entity Type

Fitness

Requirements
Must have
• LOGO

E-mail: www.silverharbourfitness.com.au

Address: 517 CORALWOOD RD EAST TALLOWAY NSW 2100
Nice to have
• Your HEALTH is your WEALTH!!!

```html
<!DOCTYPE html>
<html lang="en">
<head>
<meta charset="utf-8">
<title>Silver Harbour Fitness – Poster</title>
<link rel="stylesheet" href="https://fonts.googleapis.com/css2?family=Roboto+Condensed:wght@400;700&family=Roboto:wght@700&display=swap">
<style>
  :root {
    --ink: #111111;
    --lime: #c6d400;
    --red: #d42020;
    --gold: #c9a24a;
    --gold-dark: #a8843a;
    --blue: #1a7fc4;
    --photo-dark: #2a2623;
    --photo-mid: #6b5a4e;
    --label: #111111;
  }
  * { margin: 0; padding: 0; box-sizing: border-box; }
  html, body { width: 1200px; height: 898px; overflow: hidden; background: var(--ink); }
  .poster {
    position: relative;
    width: 1200px;
    height: 898px;
    background: var(--ink);
    font-family: "Roboto Condensed", "Arial Narrow", sans-serif;
    overflow: hidden;
  }
  .poster-shapes { position: absolute; inset: 0; }
  .brand {
    position: absolute;
    left: 640px;
    top: 70px;
    display: flex;
    align-items: center;
    gap: 34px;
  }
  .brand-mark {
    width: 150px;
    height: 150px;
    background: var(--lime);
  }
  .brand-name {
    font-family: "Roboto Condensed", "Arial Narrow", sans-serif;
    font-weight: 700;
    color: var(--gold);
    font-size: 42px;
    line-height: 1.02;
    text-transform: uppercase;
    letter-spacing: 1px;
  }
  .headline {
    position: absolute;
    left: 600px;
    width: 560px;
    text-align: center;
    font-family: "Roboto Condensed", "Arial Narrow", sans-serif;
    font-weight: 700;
    line-height: 1;
  }
  .headline-health { top: 276px; color: var(--lime); font-size: 66px; }
  .headline-wealth { top: 370px; color: var(--red); font-size: 70px; }
  .headline .caps { font-size: 1.1em; }
  .tagline {
    position: absolute;
    left: 600px;
    top: 500px;
    width: 560px;
    text-align: center;
    color: var(--gold-dark);
    font-family: "Roboto", Arial, sans-serif;
    font-weight: 700;
    font-size: 25px;
    letter-spacing: 2.5px;
    line-height: 1.6;
  }
  .contact { position: absolute; right: 22px; text-align: right; }
  .contact-label {
    color: var(--label);
    font-size: 30px;
    font-weight: 400;
  }
  .contact-value {
    color: var(--red);
    font-weight: 700;
    letter-spacing: 0.5px;
  }
  .contact-web { top: 660px; }
  .contact-web .contact-value { font-size: 40px; margin-top: 2px; }
  .contact-address { top: 790px; }
  .contact-address .contact-value { font-size: 39px; margin-top: 0; }
</style>
</head>
<body>
<main class="poster">
  <svg class="poster-shapes" width="1200" height="898" viewBox="0 0 1200 898">
    <defs>
      <linearGradient id="photoTone" x1="0" y1="0" x2="1" y2="1">
        <stop offset="0" stop-color="#8a6d5a"/>
        <stop offset="0.5" stop-color="#4a3d35"/>
        <stop offset="1" stop-color="#1c1a19"/>
      </linearGradient>
    </defs>
    <!-- lime contact band and blue base strip -->
    <polygon class="band-blue" points="0,842 620,660 1200,660 1200,898 0,898" fill="var(--blue)"/>
    <polygon class="band-lime" points="0,812 606,630 1200,630 1200,874 0,884" fill="var(--lime)"/>
    <!-- photo frame borders -->
    <polygon class="frame-gold" points="0,0 446,0 630,628 0,812" fill="var(--gold)"/>
    <polygon class="frame-red" points="0,0 438,0 620,622 0,806" fill="var(--red)"/>
    <polygon class="frame-black" points="0,0 430,0 610,616 0,800" fill="var(--ink)"/>
    <!-- photo area -->
    <polygon class="hero-photo" role="img" aria-label="Photo of a man in a gym curling a heavy dumbbell"
      points="0,0 424,0 600,612 0,792" fill="url(#photoTone)"/>
  </svg>

  <div class="brand">
    <div class="brand-mark"></div>
    <div class="brand-name">Silver<br>Harbour<br>Fitness</div>
  </div>

  <h1 class="headline headline-health">Your <span class="caps">HEALTH</span> is</h1>
  <p class="headline headline-wealth">your <span class="caps">WEALTH!!!</span></p>

  <p class="tagline">We help people look and feel<br>a million dollars</p>

  <div class="contact contact-web">
    <div class="contact-label">E-mail:</div>
    <div class="contact-value">www.silverharbourfitness.com.au</div>
  </div>
  <div class="contact contact-address">
    <div class="contact-label">Address:</div>
    <div class="contact-value">517 CORALWOOD RD EAST TALLOWAY NSW 2100</div>
  </div>
</main>
</body>
</html>
```